Brightpath Tech Partners Website Design

I have here a website mockup. If you need anything further please feel free to reach out to me! Thank you!

Current site: http://brightpathtechpartners.example/

We want it clean, concise and eye catching.

Menu: I want the same idea we used from lumivexsites.example with the logo in the middle and in the menu:

Home, About Us, How Can We Help?, Media, Blog, Contact Us.

Let's have the Social Media icons at the very top please.

For the banner - we want a pixelharbor chess image sort of like pixelharbor photo 480613927 or 31940287

I want the words "Rise Higher, Run Further, Reach Farther" to come in one at a time and then "Brightpath Tech Partners" to show up on the banner.

Maybe have "Grow Your Business with Managed IT Services from Brightpath Tech Partners" somewhere permanently on the banner that still suits everything.

Services Section: Maybe we can have them as chess pieces with something along the lines of "Make Your Next Move" - Managed IT Services, New Jersey Cloud Computing, Protect Your Business Data, Managed Email Solutions (Background 207946138)

Next Area: What sets us apart?/Testimonials (I want this as a split area) (Can we please use the banner image paralex here?)

(This is for the What Sets Us Apart side)
Outsmart threats before they reach your networks.

Outperform with the newest and latest technologies to not only keep you up and running, but to keep you at an advantage.

Reach Farther by embracing Business Continuity with Brightpath Tech Partners by your side. (I will let you choose the background for here!)

Next Area: Book Your Free Two-Hour Review! (I want a form similar to the one on the old site.)

Next area: Blogs/Sign Up for our newsletter! (Again, please choose a relevant background)

Next Area:Contact Us area with service pages. I really like the contact us part in mordavel.example where it shows the geographical area.

Target Market(s)

Business Owners in New Jersey looking to outsource their business IT, computer and network support.

Industry/Entity Type

Information Technology

Number of Pages Required

1 page

Font styles to use
Sans Serif

Requirements
Must have
• We want this website to be very sharp. I like bright colors, creative imagery.
• In the footer I must have @ 2016 Brightpath Tech Partners | Privacy Policy | Sitemap
Should not have
• I am not a fan of stuffing everything in and making it very busy. I would like clean and professional

```html
<!DOCTYPE html>
<html lang="en">
<head>
<meta charset="utf-8">
<title>Brightpath Tech Partners</title>
<link href="https://fonts.googleapis.com/css2?family=Roboto:ital,wght@0,400;0,500;0,700;1,400&family=Gochi+Hand&display=swap" rel="stylesheet">
<style>
:root{
  --navy:#1f2c48;
  --blue:#5b9bd5;
  --blue-soft:#7ea5cd;
  --accent:#3d8fd6;
  --ink:#222831;
  --muted:#6b7480;
  --pale:#f2f5f9;
  --card:#eef4fa;
  --white:#ffffff;
  --line:#d7dde4;
}
*{box-sizing:border-box;margin:0;padding:0}
html,body{width:1200px;height:2256px;overflow:hidden}
body{position:relative;font-family:"Roboto",Arial,sans-serif;color:var(--ink);background:var(--white)}

/* navigation */
.topnav{position:absolute;left:0;top:0;width:1200px;height:68px;background:var(--white);z-index:3}
.topnav a{position:absolute;top:22px;font-size:17px;color:var(--ink);text-decoration:none;letter-spacing:.2px}
.topnav a.active{color:var(--accent)}
.topnav .signup{top:20px;left:1069px;width:76px;height:24px;border-radius:4px;background:var(--blue);color:var(--white);font-weight:700;text-align:center;line-height:24px;font-size:16px}
.brand{position:absolute;left:433px;top:36px;width:283px;height:114px;background:var(--white);border-radius:0 0 10px 10px;z-index:2;display:flex;align-items:center;justify-content:center;gap:10px;box-shadow:0 2px 6px rgba(0,0,0,.15)}
.brand-dot{width:18px;height:18px;border-radius:50%;background:var(--blue)}
.brand-name{font-size:21px;font-weight:700;color:var(--navy)}

/* hero */
.hero{position:absolute;left:0;top:68px;width:1200px;height:492px;background:linear-gradient(110deg,#1b2744 0%,#27365a 55%,#3b4868 100%);overflow:hidden}
.hero-globe{position:absolute;left:33px;top:30px;width:325px;height:406px;border-radius:50%;background:radial-gradient(circle at 50% 45%,#2a5c9a 0%,#1c3a66 55%,rgba(27,39,68,0) 72%)}
.hero-lines{position:absolute;left:640px;top:132px;width:530px;font-family:"Gochi Hand",cursive;color:var(--white);font-size:52px;line-height:54px;white-space:nowrap}
.hero-lines span{display:block}
.hero-lines .l2{margin-left:45px}
.hero-lines .l3{margin-left:90px}
.hero-lines .l4{text-align:right}
.dots{position:absolute;left:568px;top:458px;display:flex;gap:10px}
.dots i{width:9px;height:9px;border-radius:50%;background:var(--white)}
.dots i:first-child{background:transparent;border:1.5px solid var(--white)}

/* services */
.service{position:absolute;top:512px;width:240px;text-align:center}
.service-icon{width:93px;height:93px;border-radius:50%;margin:0 auto;background:radial-gradient(circle at 40% 35%,#6cc0f5,#1c6fc6 75%);border:3px solid #9dd2f7}
.service h3{margin-top:14px;font-size:19px;font-weight:700;line-height:24px;color:var(--ink)}

/* apart + testimonials */
.split{position:absolute;left:0;top:681px;width:1200px;height:331px;background:var(--pale)}
.split svg{position:absolute;left:0;top:0}
.apart{position:absolute;left:126px;color:var(--white);font-weight:700;white-space:nowrap}
.people-title{position:absolute;left:820px;top:732px;font-size:24px;font-weight:700}
.people-title em{font-style:normal;color:var(--accent)}
.quote{position:absolute;left:750px;width:360px}
.avatar{position:absolute;left:0;top:12px;width:54px;height:54px;border-radius:50%;background:linear-gradient(#b89a84,#7d6a5e);border:2px solid #e4e7eb}
.quote p{margin-left:74px;font-size:11.5px;line-height:16px;font-style:italic;color:var(--muted)}
.quote b{display:block;margin:8px 0 0 74px;font-size:11.5px;font-weight:500;color:var(--ink)}

/* booking */
.booking{position:absolute;left:0;top:1015px;width:1200px;height:136px;background:#f3f5f8;border-left:2px solid var(--line);border-right:2px solid var(--line)}
.booking h2{position:absolute;left:404px;top:51px;font-size:27px;font-weight:700}
.btn{position:absolute;background:var(--blue-soft);color:var(--white);font-weight:700;text-align:center;border-radius:3px;text-transform:uppercase}
.booking .btn{left:1014px;top:48px;width:105px;height:47px;line-height:47px;font-size:13px}

/* news */
.news-title{position:absolute;left:0;top:1180px;width:1200px;text-align:center;font-size:22px;font-weight:700}
.news-title em{font-style:normal;color:var(--accent)}
.news-rule{position:absolute;left:53px;top:1220px;width:1096px;border-top:1px dashed var(--line)}
.card{position:absolute;top:1277px;width:253px;height:355px;background:var(--card)}
.card-media{height:190px}
.card h3{margin:21px 19px 0;font-size:19px;font-weight:700}
.card p{margin:10px 19px 0;font-size:14px;line-height:20px;color:var(--muted)}
.card .meta{position:absolute;left:19px;right:19px;bottom:14px;padding-top:13px;border-top:1px solid var(--line);display:flex;justify-content:space-between;font-size:11px;color:var(--muted)}
.more{left:537px;top:1669px;width:108px;height:37px;line-height:37px;font-size:13px;background:var(--blue)}

/* newsletter */
.newsletter{position:absolute;left:0;top:1727px;width:1200px;height:120px;background:#f2f4f7}
.newsletter h2{position:absolute;left:53px;top:50px;font-size:20px;font-weight:700}
.newsletter .field{position:absolute;left:415px;top:39px;width:357px;height:46px;background:var(--white);font-size:12px;color:var(--muted);text-align:center;line-height:46px}
.newsletter .btn{left:941px;top:39px;width:164px;height:46px;line-height:46px;font-size:16px;font-weight:500}

/* footer */
.footer{position:absolute;left:0;top:1847px;width:1200px;height:409px;background:var(--blue-soft);color:var(--white)}
.col{position:absolute;top:40px;width:253px}
.col h4{font-size:19px;font-weight:700;margin-bottom:16px}
.col p{font-size:13px;line-height:20px;margin-bottom:14px}
.col p.nowrap{white-space:nowrap}
.input{background:var(--white);border-radius:3px;height:32px;margin-bottom:19px;color:#8a929c;font-size:13px;padding:8px 12px}
.input.tall{height:56px}
.send{width:134px;height:34px;background:var(--white);color:var(--ink);font-size:13px;font-weight:500;text-align:center;line-height:34px;border-radius:3px}
.socials{display:flex;gap:12px;margin-top:4px}
.socials i{width:13px;height:13px;border-radius:50%;background:var(--white)}
.map{width:253px;height:211px;background:linear-gradient(135deg,#e8e4dc,#d6dbe0 60%,#c9d3de);margin-top:-6px}
.footer-rule{position:absolute;left:53px;top:359px;width:1096px;border-top:1px solid rgba(255,255,255,.6)}
.copyright{position:absolute;left:0;top:386px;width:1200px;text-align:center;font-size:13px;font-weight:500}
</style>
</head>
<body>

<nav class="topnav">
  <a class="active" style="left:53px">HOME</a>
  <a style="left:138px">ABOUT US</a>
  <a style="left:257px">HOW CAN WE HELP ?</a>
  <a style="left:762px">MEDIA</a>
  <a style="left:851px">BLOG</a>
  <a style="left:931px">CONTACT US</a>
  <a class="signup">SIGN UP</a>
</nav>

<div class="brand"><span class="brand-dot"></span><span class="brand-name">Brightpath Tech Partners</span></div>

<header class="hero">
  <div class="hero-globe" role="img" aria-label="Glowing network globe made of connected points"></div>
  <div class="hero-lines">
    <span class="l1">Rise Higher...</span>
    <span class="l2">Run Further..</span>
    <span class="l3">Reach Farther...</span>
    <span class="l4">Brightpath Tech Partners</span>
  </div>
  <div class="dots"><i></i><i></i><i></i><i></i></div>
</header>

<section class="services">
  <div class="service" style="left:59px"><div class="service-icon" role="img" aria-label="Managed IT services icon"></div><h3>Managed<br>IT Services</h3></div>
  <div class="service" style="left:339px"><div class="service-icon" role="img" aria-label="Cloud computing icon"></div><h3>New Jersey<br>Cloud Computing</h3></div>
  <div class="service" style="left:620px"><div class="service-icon" role="img" aria-label="Padlock data protection icon"></div><h3>Protect Your<br>Business Data</h3></div>
  <div class="service" style="left:900px"><div class="service-icon" role="img" aria-label="Managed email icon"></div><h3>Managed Email<br>Solutions</h3></div>
</section>

<section class="split">
  <svg width="1200" height="331" viewBox="0 0 1200 331"><polygon points="0,0 684,0 639,331 0,331" fill="#5b9bd5"/></svg>
</section>
<div class="apart" style="top:722px;font-size:33px">What Sets Us Apart?</div>
<div class="apart" style="top:787px;font-size:34px">Out Smart</div>
<div class="apart" style="top:863px;font-size:27px">Out perform</div>
<div class="apart" style="top:930px;font-size:24px">Out Host</div>

<h2 class="people-title">What <em>People Say</em></h2>
<div class="quote" style="top:776px">
  <div class="avatar" role="img" aria-label="Client portrait"></div>
  <p>Duis aute irure dolor in reprehenderit in voluptate velit esse cillum dolore eu fugiat nulla pariatur. Excepteur sint occaecat cupidatat non proident, sunt in culpa qui officia deserunt mollit.</p>
  <b>Marcus Bell, Operations Manager</b>
</div>
<div class="quote" style="top:912px">
  <div class="avatar" role="img" aria-label="Client portrait"></div>
  <p>Provident, similique sunt in culpa qui officia deserunt mollitia animi, id est laborum et dolorum fuga. Et harum quidem rerum facilis est et expedita distinctio. Nam libero tempore, cum soluta nobis.</p>
  <b>Nora Vance, Creative Designer</b>
</div>

<section class="booking">
  <h2>Book your free 2-hour review</h2>
  <div class="btn">Book now</div>
</section>

<h2 class="news-title">Latest <em>News &amp; Views</em></h2>
<div class="news-rule"></div>

<article class="card" style="left:53px">
  <div class="card-media" role="img" aria-label="Person walking with a leather bag" style="background:linear-gradient(135deg,#d9d4cc,#6b4a33)"></div>
  <h3>Standard Post</h3>
  <p>Enim congue blandit. Lorem ipsum dolor sit amet, consectetur adipiscing elit. Quisque...</p>
  <div class="meta"><span>&#9638; 22 June, 2015</span><span>&#9679; 0</span></div>
</article>
<article class="card" style="left:334px">
  <div class="card-media" role="img" aria-label="Glass coffee carafe on a table" style="background:linear-gradient(135deg,#c9c6bf,#5a4c3f)"></div>
  <h3>Video Post</h3>
  <p>Ultrices posuere cubilia curae curabitur sit amet tortor ut massa commodo. Vestibulum...</p>
  <div class="meta"><span>&#9638; 22 June, 2015</span><span>&#9679; 0</span></div>
</article>
<article class="card" style="left:615px">
  <div class="card-media" role="img" aria-label="Cafe table and chair by a brick wall" style="background:linear-gradient(135deg,#6e4a38,#b49474)"></div>
  <h3>Post with Image</h3>
  <p>Enim congue blandit. Lorem ipsum dolor sit amet, consectetur adipiscing elit. Quisque...</p>
  <div class="meta"><span>&#9638; 22 June, 2015</span><span>&#9679; 0</span></div>
</article>
<article class="card" style="left:896px">
  <div class="card-media" role="img" aria-label="Dark still life of a bag and objects" style="background:linear-gradient(135deg,#2c3644,#485563)"></div>
  <h3>Image Post</h3>
  <p>Ultrices posuere cubilia curae curabitur sit amet tortor ut massa commodo. Vestibulum...</p>
  <div class="meta"><span>&#9638; 22 June, 2015</span><span>&#9679; 3</span></div>
</article>

<div class="btn more">View more</div>

<section class="newsletter">
  <h2>SUBSCRIBE TO NEWLLETTER</h2>
  <div class="field">Put your email address here</div>
  <div class="btn">Subscribe</div>
</section>

<footer class="footer">
  <div class="col" style="left:53px">
    <h4>Contact Us</h4>
    <p>Maecenas etos sit amet, consectetur adipiscing elit. Terminal volutpat rutrum metro amet sollicitudin interdum.</p>
    <p><b>Phone:</b> (973) 555-0148</p>
    <p class="nowrap"><b>Office:</b> 48 Orchard Lane, Fairfield NJ 07004</p>
    <p class="nowrap"><b>Email:</b> info@brightpathtech.example</p>
    <div class="socials"><i></i><i></i><i></i><i></i><i></i></div>
  </div>
  <div class="col" style="left:334px">
    <h4>Feel Free to Mail</h4>
    <div class="input">Name *</div>
    <div class="input">Email *</div>
    <div class="input tall">Write Your Message Here...</div>
    <div class="send">SEND MESSAGE</div>
  </div>
  <div class="col" style="left:615px">
    <h4>Headquarters</h4>
    <div class="map" role="img" aria-label="Street map showing the headquarters location"></div>
  </div>
  <div class="col" style="left:896px">
    <h4>About Team</h4>
    <p>Enim congue blandit. Lorem ipsum dolor sit amet, consectetur adipiscing elit. Quisque consectetur interdum finibus. Vestibulum ante ipsum primis in faucibus orci. luctus et ultrices posuere.</p>
    <p>Cubilia cras blandit finibus ipsum, id porttitor arcu volutpat a. Integer iaculis erat nec justo malesuada faucibus vel tempus sapien. Vivamus aliquam euismod tristique.</p>
  </div>
  <div class="footer-rule"></div>
  <div class="copyright">Copyright © 2016 Brightpath Tech Partners. All rights reserved.</div>
</footer>

</body>
</html>
```